Home Services- Spring Clean Options

Brightwell Crew provides a variety of Home Services- focused on cleaning & improving the exterior of the home:

 Power Washing- driveways, sidewalks, patios, decks, fence
 Fence Staining- make fence look new with variety of staining colors
 Gutter cleaning- important to make sure have proper Water Drainage
 Gutter Guard Installation- prevent damage to roof and house by keeping debris out of gutters and water flowing.
 Window Washing- our exterior washing team and reach the highest windows
 Landscape& Patio Lights- highlight areas for beauty and safety
Updates

We are are almost finished. Just please make sure you pay attention to the wording and grammer in Red thx

Target Market(s)

Middle to Upper level Home Owners (especially women)

Industry/Entity Type

Cleaning Services

Font styles to use
Serif
Sans Serif

Requirements
Must have
• Not be Cluttered- Clean friendly, professional look. Focus on the Professional

Info@GoBrightwellCrew.com
972-648-0000
Nice to have
• Pictures of services- these are just examples
Should not have
• Bigger and bolder Services & Specials. Want to Show all the Services we offer but do Not use too much detail- don't want it to look "cluttered"

```html
<!DOCTYPE html>
<html lang="en">
<head>
<meta charset="utf-8">
<title>Cleaning &amp; Improving the Exterior – Service Flyer</title>
<link rel="stylesheet" href="https://fonts.googleapis.com/css2?family=Exo+2:wght@800;900&family=Lato:wght@400;700;900&display=swap">
<style>
  :root {
    --backdrop: #d9d9db;
    --paper: #f4f4f5;
    --brand-red: #a31b1f;
    --deep-red: #7e1114;
    --photo-red: #b7382c;
    --photo-red-dark: #7c1f17;
    --slate: #3a3b40;
    --slate-light: #6b6c72;
    --ink: #4a4a4e;
    --white: #ffffff;
  }
  * { box-sizing: border-box; margin: 0; padding: 0; }
  html, body { width: 1200px; height: 1200px; overflow: hidden; }
  body {
    background: var(--backdrop);
    font-family: "Lato", sans-serif;
  }
  .flyer {
    position: absolute;
    left: 200px; top: 35px;
    width: 800px; height: 1130px;
    background: var(--paper);
    overflow: hidden;
    box-shadow: 0 10px 30px rgba(0,0,0,.18);
  }
  .flyer-shapes { position: absolute; inset: 0; }
  .headline {
    position: absolute;
    left: 290px; top: 410px;
    width: 370px;
    text-align: center;
    color: var(--white);
    font-family: "Exo 2", sans-serif;
    font-weight: 900;
    font-size: 44px;
    line-height: 1.04;
    letter-spacing: 1px;
    text-transform: uppercase;
    text-shadow: 0 3px 6px rgba(0,0,0,.35);
  }
  .services {
    position: absolute;
    left: 50px; top: 640px;
    width: 380px;
    list-style: none;
  }
  .service { margin-bottom: 8px; }
  .service-name {
    display: block;
    color: var(--brand-red);
    font-weight: 900;
    font-size: 20px;
    line-height: 1.05;
    text-transform: uppercase;
  }
  .service-note {
    display: block;
    color: var(--ink);
    font-size: 12.5px;
    line-height: 1.2;
  }
  .contact-phone {
    position: absolute;
    left: 26px; top: 1069px;
    color: var(--white);
    font-weight: 700;
    font-size: 28px;
    letter-spacing: 1px;
    white-space: nowrap;
  }
  .contact-web {
    position: absolute;
    right: 30px; top: 1100px;
    color: var(--white);
    font-weight: 700;
    font-size: 13px;
    letter-spacing: 1px;
    text-transform: uppercase;
    white-space: nowrap;
  }
</style>
</head>
<body>
<article class="flyer">
  <svg class="flyer-shapes" viewBox="0 0 800 1130" width="800" height="1130">
    <defs>
      <linearGradient id="outdoor-tone" x1="0" y1="0" x2="1" y2="1">
        <stop offset="0" stop-color="#7c1f17"/>
        <stop offset=".55" stop-color="#b7382c"/>
        <stop offset="1" stop-color="#7c1f17"/>
      </linearGradient>
      <linearGradient id="window-tone" x1="0" y1="0" x2="1" y2="1">
        <stop offset="0" stop-color="#c9a08e"/>
        <stop offset="1" stop-color="#8a5a48"/>
      </linearGradient>
    </defs>

    <g class="corner-strips">
      <polygon points="0,0 190,0 0,110" fill="var(--slate-light)"/>
      <polygon points="640,0 800,0 800,150" fill="var(--deep-red)"/>
    </g>

    <polygon class="photo-patio" role="img" aria-label="Photo: family dining on a patio while a crew member works outdoors"
             points="70,40 800,40 800,430 480,720 20,250"
             fill="url(#outdoor-tone)"/>

    <g class="frame-accents" fill="none" stroke="var(--white)" stroke-width="5">
      <rect x="245" y="155" width="120" height="120" rx="16" transform="rotate(45 305 215)"/>
      <rect x="710" y="430" width="110" height="110" rx="16" transform="rotate(45 765 485)"/>
    </g>

    <g class="diagonal-bands">
      <polygon points="0,230 40,230 300,560 260,560" fill="var(--slate)"/>
      <polygon points="650,560 800,430 800,470 690,570" fill="var(--slate)"/>
      <polygon points="520,680 700,560 712,574 532,694" fill="var(--brand-red)"/>
    </g>

    <polygon class="photo-window" role="img" aria-label="Photo: hand washing a window pane"
             points="440,760 800,500 800,1050 600,1050"
             fill="url(#window-tone)"/>
    <polygon points="420,760 800,480 800,500 440,776" fill="var(--slate)"/>

    <g class="footer-band">
      <rect x="0" y="1050" width="800" height="80" fill="var(--brand-red)"/>
      <polygon points="0,1050 330,1050 370,1090 330,1130 0,1130" fill="var(--deep-red)"/>
      <polygon points="330,1050 390,1050 430,1090 370,1090" fill="var(--slate)"/>
    </g>
  </svg>

  <h1 class="headline">Cleaning<br>&amp; Improving<br>the<br>Exterior</h1>

  <ul class="services">
    <li class="service"><span class="service-name">Power Washing</span><span class="service-note">driveways, sidewalks, patios, decks, fence</span></li>
    <li class="service"><span class="service-name">Fence Staining</span><span class="service-note">make fence look new with variety of staining colors</span></li>
    <li class="service"><span class="service-name">Gutter Cleaning</span><span class="service-note">important to make sure have proper Water Drainage</span></li>
    <li class="service"><span class="service-name">Gutter Guard Installation</span><span class="service-note">prevent damage to roof and house by keeping debris out of gutters and water flowing.</span></li>
    <li class="service"><span class="service-name">Window Washing</span><span class="service-note">our exterior washing team and reach the highest windows</span></li>
    <li class="service"><span class="service-name">Landscape&amp; Patio Lights</span><span class="service-note">highlight areas for beauty and safety</span></li>
  </ul>

  <p class="contact-phone">(+9) 012-345-6789</p>
  <p class="contact-web">E: yourmail@email.com | www.yourwebsite.com</p>
</article>
</body>
</html>
```